Stationary Design - KM Facial Plastics

We are looking for a stylish and professional stationary design for a facial plastic surgeon. The stationary design will be for letterhead, business card, appointment cards and envelopes.
The design must be slick and aesthetically pleasing whilst incorporating the style of our logo as attached below.

Target Market(s)

Adults of all ages

Font styles to use
Serif
Script

Requirements
Must have
• Must be an aesthetically pleasing, stylish and professional design that includes the required information in a captivating layout.
• Must also be welcoming with a balanced design and a clean crisp finish.
• Details should include:
• Mr Dorian Halvet - Consultant Otolaryngologist & Facial Plastic Surgeon
• Phone: 03 5917 2846
• Fax: 03 5918 4072
• Email: info@kmfacialplastics.example.au
• Consulting from: Bendigo, Echuca, Epping, Waverley & Melbourne CBD
• Appointment Card should include:
• Date, time, fee and location as per the attached example.
• location addresses are:
• 41 Marlow Street Echuca Vic 3564
• 318 Bramble Street Bendigo Vic 3550
• Level 3, 612 Hadley Street, Epping Vic 3076
• Level 6, 480 Tennant Street Melbourne Vic 3000
Should not have
• Clutter

```html
<!DOCTYPE html>
<html lang="en">
<head>
<meta charset="utf-8">
<title>KM Facial Plastics – Appointment Card</title>
<link rel="stylesheet" href="https://fonts.googleapis.com/css2?family=Noto+Serif:ital,wght@0,400;0,700;1,400&family=Roboto:wght@400&display=swap">
<style>
  :root {
    --backdrop: #d1d2d4;
    --card-light: #ffffff;
    --card-dark: #3f3f40;
    --ink: #3a3a3a;
    --rule: #a9a9a9;
    --mark-faint: #d6d6d6;
    --mark-light: #ffffff;
    --shadow: rgba(0, 0, 0, 0.35);
  }
  * { margin: 0; padding: 0; box-sizing: border-box; }
  html, body {
    width: 1200px; height: 1200px; overflow: hidden;
    background: var(--backdrop);
  }
  .stage { position: relative; width: 1200px; height: 1200px; }
  .card {
    position: absolute; left: 224px; width: 752px; height: 430px;
    box-shadow: 6px 8px 8px var(--shadow);
  }
  .card--front { top: 157px; background: var(--card-light); color: var(--ink); }
  .card--back { top: 613px; background: var(--card-dark); }

  .card-title {
    position: absolute; top: 45px; left: 0; right: 0; text-align: center;
    font-family: "Noto Serif", serif; font-weight: 700; font-size: 32px;
    line-height: 1; letter-spacing: 6.5px; color: var(--ink);
  }
  .field-label, .field-meridiem, .locations-heading {
    position: absolute; line-height: 1; white-space: nowrap;
    font-family: "Noto Serif", serif; font-size: 20px; color: var(--ink);
  }
  .field-label { left: 69px; }
  .field-label--date { top: 119px; }
  .field-label--time { top: 165px; }
  .field-label--fee { top: 209px; }
  .field-meridiem { top: 164px; left: 574px; font-size: 21px; font-style: italic; word-spacing: 6px; }

  .field-rule { position: absolute; height: 0; border-top: 1.5px solid var(--rule); }
  .field-rule--date { top: 136px; left: 142px; width: 542px; }
  .field-rule--time { top: 181px; left: 152px; width: 406px; }
  .field-rule--fee { top: 227px; left: 158px; width: 526px; }

  .locations-heading { top: 253px; left: 0; right: 0; text-align: center; font-weight: 400; }

  .location-list { position: absolute; top: 296px; left: 69px; list-style: none; }
  .location-list li {
    display: flex; align-items: center; height: 33.5px; line-height: 1;
    font-family: "Roboto", sans-serif; font-size: 19px; color: var(--ink);
    white-space: nowrap;
  }
  .location-list li { align-items: flex-start; }
  .checkbox {
    width: 13px; height: 13px; border: 1.3px solid var(--ink);
    margin-right: 5px; margin-top: 3px; flex: none;
  }

  .brand-faint {
    position: absolute; left: 546px; top: 253px; width: 132px; height: 132px;
    border: 1.5px solid var(--mark-faint); border-radius: 50%;
    display: flex; align-items: center; justify-content: center; text-align: center;
    font-family: "Noto Serif", serif; font-size: 15px; line-height: 1.3;
    color: var(--mark-faint);
  }
  .brand-main {
    position: absolute; left: 252px; top: 77px; width: 276px; height: 276px;
    border: 3px solid var(--mark-light); border-radius: 50%;
    display: flex; align-items: center; justify-content: center; text-align: center;
    font-family: "Noto Serif", serif; font-size: 30px; line-height: 1.25;
    color: var(--mark-light);
  }
</style>
</head>
<body>
<main class="stage">
  <section class="card card--front" aria-label="Appointment card, front">
    <h1 class="card-title">APPOINTMENT CARD</h1>

    <span class="field-label field-label--date">DATE :</span>
    <span class="field-rule field-rule--date"></span>

    <span class="field-label field-label--time">TIME :</span>
    <span class="field-rule field-rule--time"></span>
    <span class="field-meridiem">a.m. p.m.</span>

    <span class="field-label field-label--fee">FREE :</span>
    <span class="field-rule field-rule--fee"></span>

    <h2 class="locations-heading">Location Addresses :</h2>
    <ul class="location-list">
      <li><span class="checkbox"></span>318 Bramble Street Bendigo Vic 3550</li>
      <li><span class="checkbox"></span>Level 6, 480 Tennant Street Melbourne Vic 3000</li>
      <li><span class="checkbox"></span>Level 3, 612 Hadley Street, Epping Vic 3076</li>
    </ul>

    <div class="brand-faint">KM Facial<br>Plastics</div>
  </section>

  <section class="card card--back" aria-label="Appointment card, back">
    <div class="brand-main">KM Facial<br>Plastics</div>
  </section>
</main>
</body>
</html>
```